Postcard

I'm a realtor looking to create a general postcard for my business to be mailed out to homeowners. I have a good idea of what I'm looking for, just need someone to put it all together and make it look good. Please keep colors similar to the logo. The save money symbol can be different colors to help stand out. File #6 is the theme for the bottom section of file #5.

Realtor

```html
<!DOCTYPE html>
<html lang="en">
<head>
<meta charset="utf-8">
<title>Harrow Realty Postcard</title>
<link href="https://fonts.googleapis.com/css2?family=Source+Sans+3:ital,wght@0,400;0,600;0,700;1,800&family=Montserrat:wght@500&display=swap" rel="stylesheet">
<style>
  :root {
    --navy: #1f3f91;
    --royal: #2848a6;
    --brand-text: #2d4aa0;
    --sky: #0a9ae0;
    --mist: #e8f1f9;
    --sun: #fff200;
    --white: #ffffff;
  }
  * { margin: 0; padding: 0; box-sizing: border-box; }
  html, body { width: 1200px; height: 784px; overflow: hidden; background: var(--white); }
  body { position: relative; font-family: "Source Sans 3", "Helvetica Neue", Arial, sans-serif; }

  .postcard {
    position: absolute; left: 46px; top: 29px; width: 1108px; height: 702px;
    background: linear-gradient(90deg, var(--mist) 0%, #b6d7f0 22%, var(--sky) 52%, #1477c9 72%, var(--royal) 100%);
    box-shadow: 8px 18px 26px rgba(10, 20, 60, 0.35);
    overflow: hidden;
  }
  .postcard::after {
    content: ""; position: absolute; inset: 0;
    background: linear-gradient(180deg, rgba(20,50,140,0.35) 0%, rgba(20,50,140,0) 30%);
    pointer-events: none;
  }

  .house-mark {
    position: absolute; left: 0; top: 380px; width: 250px; height: 260px;
    background: linear-gradient(180deg, rgba(70,100,180,0.35), rgba(70,100,180,0.15));
    border-radius: 110px 110px 0 0;
  }

  .brand-block {
    position: absolute; left: 0; top: 0; width: 578px; height: 329px; z-index: 2;
    box-shadow: 6px 10px 18px rgba(10, 20, 60, 0.45);
  }
  .brand-block .top-band { height: 27px; background: var(--sun); }
  .brand-block .name-panel {
    height: 230px; background: var(--navy);
    display: flex; align-items: center; justify-content: center;
  }
  .brand-name { color: var(--white); font-weight: 600; font-size: 62px; letter-spacing: 1px; }
  .phone-band {
    height: 72px; background: var(--sun); overflow: hidden;
    display: flex; align-items: center; justify-content: center;
    color: var(--brand-text); font-weight: 800; font-style: italic; font-size: 86px; line-height: 1;
  }

  .offer {
    position: absolute; left: 0; width: 560px; text-align: center;
    color: var(--brand-text); line-height: 1; white-space: nowrap; z-index: 1;
  }
  .offer.rate { top: 364px; font-size: 47px; }
  .offer.includes { top: 447px; font-size: 48px; letter-spacing: -0.4px; }
  .offer.photo { top: 523px; font-size: 52px; letter-spacing: -0.4px; }

  .headline {
    position: absolute; left: 586px; top: 14px; z-index: 2; line-height: 1; white-space: nowrap;
    color: var(--white); font-weight: 800; font-style: italic; font-size: 90px; letter-spacing: -1px;
    text-shadow: 8px 8px 14px rgba(10, 20, 60, 0.55);
  }
  .headline .dollar { font-size: 126px; vertical-align: -12px; margin-right: -8px; }

  .features {
    position: absolute; left: 650px; top: 0; list-style: none; z-index: 2;
    color: var(--white); font-size: 29px; line-height: 1.15;
  }
  .features li { position: absolute; white-space: nowrap; }

  .footer-band {
    position: absolute; left: 0; bottom: 0; width: 100%; height: 87px; z-index: 2;
    background: var(--royal); line-height: 1; white-space: nowrap;
    display: flex; align-items: center; justify-content: center;
    font-family: "Montserrat", "Helvetica Neue", Arial, sans-serif; font-weight: 500;
    color: var(--white); font-size: 92px;
    text-shadow: 6px 8px 10px rgba(5, 10, 40, 0.6);
  }
</style>
</head>
<body>
  <div class="postcard">
    <div class="house-mark" role="img" aria-label="Faint house with dollar sign decoration"></div>

    <div class="brand-block">
      <div class="top-band"></div>
      <div class="name-panel"><span class="brand-name">Harrow Realty, LLC</span></div>
      <div class="phone-band">555.201.4477</div>
    </div>

    <p class="offer rate">Unbeatable 3.5%</p>
    <p class="offer includes">Full Service Listings Include</p>
    <p class="offer photo">Professional Photography</p>

    <h1 class="headline"><span class="dollar">$</span>AVE MONEY</h1>

    <ul class="features">
      <li style="top:127px">Full Color Brochures</li>
      <li style="top:171px">Digital Floor Plans</li>
      <li style="top:216px">Personalized Website</li>
      <li style="top:258px">Featured Listing on Abode &amp; Nestly</li>
      <li style="top:305px">Full MLS Benefits</li>
      <li style="top:348px">Open House</li>
      <li style="top:386px">Sign Post in Yard</li>
      <li style="top:427px">Solar Power Brochure Box</li>
      <li style="top:473px; line-height:1">Addition Discount<br>for Unrepresented Buyers</li>
      <li style="top:556px">Expert Negotiations</li>
    </ul>

    <div class="footer-band">Much , Much More!</div>
  </div>
</body>
</html>
```